Grafik für Gerüstplane
Zielgruppe
Wir sind ein Malermeisterbetrieb mit Arbeitsbühnenverleih und bieten hochwertige und moderne Malerarbeiten für Gewerbe- und Privatkunden an.
Aufgabenstellung
Es wird eine moderne Grafik/Design für eine Gerüstplane benötigt. Die Gerüstplane sollte zum Corporate Design passen. Außerdem sollte der Schriftzug 'Arbeitsbühnenverleih' sowie meine Kontaktdaten (E-mail, Website und Handynummer) mit auf der Gerüstplane integriert werden.
Die Größe der Gerüstplane ist bereits vorgegeben, und es wird nur die Grafik benötig! Die Plane ist 2,05Meter * 2.00 Meter groß und die unteren 2/3 der Fläche dienen als Werbefläche für mich. (Vorlage im Anhang als PDF)
Ich freue mich auf eure kreativen Ideen! :-) Weitere Projekte sind in Planung.

```html
<!DOCTYPE html>
<html lang="de">
<head>
<meta charset="utf-8">
<title>Gerüstplane Malermeister Korbinian Feldner</title>
<link rel="stylesheet" href="https://fonts.googleapis.com/css2?family=Ubuntu:ital,wght@0,400;0,500;0,700;1,400&family=Cinzel:wght@400&display=swap">
<style>
  :root {
    --red: #e30613;
    --blue-dark: #1b56a8;
    --blue-light: #2d9fdc;
    --white: #ffffff;
    --ink: #111111;
    --page: #f2f2f2;
  }
  * { box-sizing: border-box; margin: 0; padding: 0; }
  html, body { width: 849px; height: 1200px; overflow: hidden; background: var(--page); }
  body { font-family: "Ubuntu", sans-serif; position: relative; }

  .banner {
    position: absolute; left: 19.5px; top: 183px; width: 810px; height: 834px;
    background: var(--white); box-shadow: 0 6px 16px rgba(0,0,0,.25); overflow: hidden;
  }

  /* Blue header band */
  .header { position: absolute; left: 0; top: 0; width: 810px; height: 315px; }
  .header-art {
    position: absolute; inset: 0;
    background: linear-gradient(180deg, var(--blue-dark) 0%, #2378c6 55%, var(--blue-light) 100%);
  }
  .partner-name {
    position: absolute; left: 550px; top: 34px; width: 234px; text-align: right;
    font-weight: 700; font-size: 38px; color: var(--white); letter-spacing: 0.5px;
  }
  .partner-claim {
    position: absolute; left: 550px; top: 98px; width: 234px; text-align: right;
    font-size: 12.5px; font-weight: 500; color: var(--white);
  }
  .header-claim {
    position: absolute; left: 252px; top: 272px; font-size: 31px; font-weight: 700;
    color: var(--white); letter-spacing: 0.5px; white-space: nowrap;
  }
  .flag { position: absolute; left: 733px; top: 273px; }

  /* White contact area */
  .contact { position: absolute; left: 0; top: 315px; width: 491px; height: 519px; }
  .brand {
    position: absolute; left: 0; top: 60px; width: 491px;
    display: flex; align-items: center; justify-content: center; gap: 14px;
  }
  .brand-dot { width: 40px; height: 40px; border-radius: 50%; background: var(--red); }
  .brand-name { font-weight: 700; font-size: 52px; color: var(--red); }
  .title-row {
    position: absolute; left: 26px; top: 205px; width: 443px;
    display: flex; align-items: center; gap: 14px;
  }
  .title-row .rule { flex: 1; height: 5px; border-top: 1.5px solid var(--red); border-bottom: 1.5px solid var(--red); }
  .title-row span { font-family: "Cinzel", serif; font-size: 22px; color: var(--red); }
  .owner {
    position: absolute; left: 26px; top: 228px; width: 443px; text-align: center;
    font-family: "Cinzel", serif; font-weight: 400; font-size: 36px; color: var(--ink); white-space: nowrap; letter-spacing: -0.5px;
  }
  .line { position: absolute; left: 26px; display: flex; align-items: flex-start; gap: 10px; color: var(--ink); white-space: nowrap; }
  .line svg { flex: none; }
  .phone { top: 280px; font-size: 33px; font-weight: 700; align-items: center; }
  .address { top: 334px; font-size: 23px; line-height: 33px; }
  .mail { top: 401px; font-size: 23px; align-items: center; }
  .web { top: 446px; font-size: 27px; font-weight: 700; align-items: center; }

  /* Red services area */
  .services { position: absolute; left: 491px; top: 315px; width: 319px; height: 519px; background: var(--red); color: var(--white); }
  .lift-art {
    position: absolute; left: 103px; top: 35px; width: 104px; height: 120px;
    background: rgba(255,255,255,.85); border-radius: 6px;
  }
  .services h2 {
    position: absolute; left: 0; top: 163px; width: 319px; text-align: center;
    font-size: 34px; font-weight: 700; line-height: 33px;
  }
  .service-list { position: absolute; left: 24px; top: 247px; list-style: none; }
  .service-list li {
    position: relative; padding-left: 34px; font-size: 20px; font-weight: 500;
    line-height: 25px; margin-bottom: 11px;
  }
  .service-list li::before {
    content: ""; position: absolute; left: 2px; top: 5px; width: 16px; height: 16px;
    border-radius: 50%; background: var(--white);
  }
  .badge {
    position: absolute; left: 430px; top: 337px; width: 130px; height: 130px; border-radius: 50%;
    background: var(--white); border: 3px solid var(--red); box-shadow: 2px 3px 6px rgba(0,0,0,.3);
    display: flex; flex-direction: column; align-items: center; justify-content: center;
    color: var(--red); transform: rotate(-12deg); font-weight: 700; line-height: 1;
  }
  .badge .small { font-size: 26px; }
  .badge .big { font-size: 44px; transform: scaleX(.8); letter-spacing: -1px; }
</style>
</head>
<body>
  <main class="banner">
    <section class="header">
      <div class="header-art" role="img" aria-label="Blaue Hintergrundgrafik mit stilisierten Motiven des Holzschutz-Partners"></div>
      <p class="partner-name">NORDLACK</p>
      <p class="partner-claim">Nordlack schützt Werte</p>
      <p class="header-claim">Holzschutz aus Norwegen</p>
      <svg class="flag" width="51" height="32" viewBox="0 0 22 16" aria-label="Norwegische Flagge" role="img">
        <rect width="22" height="16" fill="#ba0c2f"/>
        <rect x="6" width="4" height="16" fill="#fff"/>
        <rect y="6" width="22" height="4" fill="#fff"/>
        <rect x="7" width="2" height="16" fill="#00205b"/>
        <rect y="7" width="22" height="2" fill="#00205b"/>
      </svg>
    </section>

    <section class="contact">
      <div class="brand"><span class="brand-dot"></span><span class="brand-name">Feldner</span></div>
      <div class="title-row"><i class="rule"></i><span>MALERMEISTER</span><i class="rule"></i></div>
      <h1 class="owner">KORBINIAN FELDNER</h1>

      <p class="line phone">
        <svg width="28" height="28" viewBox="0 0 24 24"><rect x="1" y="1" width="22" height="22" rx="5" fill="var(--red)"/><path d="M8 6.5c.6-.6 1.3-.5 1.6.1l1 1.8c.3.5.1 1-.3 1.3l-.6.5c.6 1.4 1.7 2.5 3.1 3.1l.5-.6c.3-.4.8-.6 1.3-.3l1.8 1c.6.3.7 1 .1 1.6-2.4 2.4-10.9-6.1-8.5-8.5z" fill="#fff"/></svg>
        0170/4826391
      </p>
      <p class="line address">
        <svg width="30" height="44" viewBox="0 0 24 34"><path d="M12 1C6 1 2 5.4 2 11c0 7 10 22 10 22s10-15 10-22C22 5.4 18 1 12 1z" fill="var(--red)"/><circle cx="12" cy="11" r="4" fill="#fff"/></svg>
        <span>Am Lindenanger 12<br>82999 Birkach am Weiher</span>
      </p>
      <p class="line mail">
        <svg width="30" height="22" viewBox="0 0 30 22"><rect width="30" height="22" rx="2" fill="var(--red)"/><path d="M2 3l13 10L28 3" stroke="#fff" stroke-width="2.5" fill="none"/></svg>
        info@malerbetrieb-feldner.de
      </p>
      <p class="line web">
        <svg width="30" height="30" viewBox="0 0 30 30" fill="none" stroke="var(--red)" stroke-width="2.4"><circle cx="15" cy="15" r="13"/><ellipse cx="15" cy="15" rx="6" ry="13"/><path d="M2 15h26M4 8h22M4 22h22M15 2v26"/></svg>
        www.feldner-malerbetrieb.de
      </p>
    </section>

    <section class="services">
      <div class="lift-art" role="img" aria-label="Symbol eines LKW mit Hubarbeitsbühne"></div>
      <h2>Arbeitsbühnen-<br>verleih</h2>
      <ul class="service-list">
        <li>Holzschutzarbeiten</li>
        <li>Lackier- und<br>Lasurarbeiten</li>
        <li>Fassadenanstriche</li>
        <li>Innenraumgestaltung</li>
        <li>Kreative<br>Oberflächengestaltung</li>
        <li>Spachtelarbeiten</li>
      </ul>
    </section>

    <div class="badge"><span class="small">Jetzt</span><span class="big">NEU:</span></div>
  </main>
</body>
</html>
```